Flyer für Hausärzte
Aufgabenstellung
Der Flyer soll das Format DIN 105 lang haben und später bei druckfalter.de gedruckt werden. Entsprechende Vorlagen sind bei druckfalter.de vorhanden. Der Flyer wird in der Mitte 1x gefalzt und beidseitige bedruckt. (Es gibt also eine Außenseite, eine Doppel Innenseiten und eine Rückseite)
Der Flyer soll Neupatienten sowie BEstandspatienten ansprechen und über die Ärzte und die Leistungen informieren. Siehe www.praxis-lindenbogen.de
Die Fotos auf der Homepage können verwendet werden, entsprechende Lizenzen für die Nutzung liegen vor. An besseren Ideen bin ich natürlich auch interessiert :-)
Datenübergabe in Adobe Illustrator (.ai) oder Adobe InDesign (.indd)
Vielen Dank und beste Grüße

```html
<!DOCTYPE html>
<html lang="de">
<head>
<meta charset="utf-8">
<title>Hausarztpraxis – Innenseite</title>
<link rel="stylesheet" href="https://fonts.googleapis.com/css2?family=Montserrat:wght@400;600&family=Sacramento&display=swap">
<style>
  :root{
    --pink:#e0358f;
    --ink:#1d1d1f;
    --rule:#4a4f57;
    --paper:#ffffff;
    --photo-doctor:linear-gradient(135deg,#e6ecf2 0%,#d9c7d8 45%,#e58fbd 75%,#d0607f 100%);
    --photo-family:linear-gradient(160deg,#eceae6 0%,#d9cfc4 40%,#c8b3a0 65%,#e9e6e2 100%);
  }
  *{box-sizing:border-box;margin:0;padding:0}
  html,body{width:1200px;height:1200px;overflow:hidden;background:var(--paper)}
  .spread{position:relative;width:1200px;height:1200px;border:1px solid var(--rule);font-family:"Montserrat",Arial,sans-serif;color:var(--ink)}
  .fold{position:absolute;left:600px;top:0;width:1px;height:100%;background:var(--rule)}
  .script-title{position:absolute;font-family:"Sacramento",cursive;color:var(--pink);font-size:64px;line-height:1;font-weight:400}
  .title-help{left:40px;top:166px}
  .title-services{left:638px;top:590px}
  .promise{position:absolute;left:40px;width:540px}
  .promise h3{color:var(--pink);font-size:19px;font-weight:600;line-height:26px}
  .promise p{font-size:19px;line-height:26px;letter-spacing:.2px}
  .photo{position:absolute}
  .photo-family{left:0;top:614px;width:529px;height:477px;background:var(--photo-family)}
  .photo-doctor{left:601px;top:113px;width:506px;height:416px;background:var(--photo-doctor)}
  .photo::after{content:"";position:absolute;left:0;right:0;bottom:0;height:30px;background:rgba(255,255,255,.45)}
  .cross{position:absolute;width:80px;height:80px}
  .cross-family{left:478px;top:584px}
  .cross-doctor{left:1059px;top:84px}
  .services{position:absolute;left:645px;top:674px;list-style:none}
  .services li{display:flex;align-items:center;height:68.7px;font-size:23px;letter-spacing:.3px}
  .services svg{width:56px;height:56px;margin-right:26px;flex:none}
</style>
</head>
<body>
<div class="spread">
  <div class="fold"></div>

  <h2 class="script-title title-help">Wie können wir helfen?</h2>

  <div class="promise" style="top:244px">
    <h3>Wir sind Ihr Ansprechpartner</h3>
    <p>Als Hausärzte sind wir in allen Gesundheitsfragen<br>Ihre erste Anlaufstelle</p>
  </div>
  <div class="promise" style="top:348px">
    <h3>Wir sind Ihr Koordinator</h3>
    <p>Wir behalten den Überblick und leiten<br>Untersuchungen für Sie in die Wege</p>
  </div>
  <div class="promise" style="top:453px">
    <h3>Wir begleiten Sie</h3>
    <p>Wir beraten Sie und unterstützen Sie dabei wieder<br>gesund zu werden und zu bleiben</p>
  </div>

  <div class="photo photo-family" role="img" aria-label="Foto: drei Generationen einer Familie lächeln gemeinsam auf einem Sofa"></div>
  <svg class="cross cross-family" viewBox="0 0 80 80" aria-hidden="true">
    <path d="M26 8h22v22h22v22H48v22H26V52H4V30h22z" fill="#fff"/>
    <path d="M30 4h16v24h24v16H46v24H30V44H6V28h24z" fill="var(--pink)"/>
  </svg>

  <div class="photo photo-doctor" role="img" aria-label="Foto: Ärztin in pinker Kleidung hält ein Stethoskop nach vorn"></div>
  <svg class="cross cross-doctor" viewBox="0 0 80 80" aria-hidden="true">
    <path d="M26 8h22v22h22v22H48v22H26V52H4V30h22z" fill="#fff"/>
    <path d="M30 4h16v24h24v16H46v24H30V44H6V28h24z" fill="var(--pink)"/>
  </svg>

  <h2 class="script-title title-services">Unsere Leistungen</h2>

  <ul class="services">
    <li><svg viewBox="0 0 56 56" fill="none" stroke="var(--pink)" stroke-width="1.6"><circle cx="28" cy="28" r="26.5"/><circle cx="28" cy="21" r="6"/><path d="M17 41c0-7 5-11 11-11s11 4 11 11z"/><path d="M23 31v5a3 3 0 0 0 6 0"/></svg>Checkup und Checkup Plus</li>
    <li><svg viewBox="0 0 56 56" fill="none" stroke="var(--pink)" stroke-width="1.6"><circle cx="28" cy="28" r="26.5"/><rect x="14" y="17" width="28" height="18" rx="1.5"/><path d="M18 27h6l2-5 3 9 2-4h7"/><path d="M24 40h8M28 35v5"/></svg>Ruhe-EKG/Belastungs-EKG</li>
    <li><svg viewBox="0 0 56 56" fill="none" stroke="var(--pink)" stroke-width="1.6"><circle cx="28" cy="28" r="26.5"/><circle cx="22" cy="21" r="6"/><path d="M22 21l3-3"/><path d="M22 27v8a6 6 0 0 0 12 0v-4"/><ellipse cx="34" cy="26" rx="4" ry="5"/></svg>24h-Blutdruckmessung</li>
    <li><svg viewBox="0 0 56 56" fill="none" stroke="var(--pink)" stroke-width="1.6"><circle cx="28" cy="28" r="26.5"/><rect x="15" y="15" width="20" height="18" rx="1.5"/><path d="M19 27q6-9 12 0"/><path d="M20 33v8h8v-8"/><path d="M38 24h4l-1 6h-2z"/></svg>Ultraschalluntersuchung</li>
    <li><svg viewBox="0 0 56 56" fill="none" stroke="var(--pink)" stroke-width="1.6"><circle cx="28" cy="28" r="26.5"/><path d="M28 14v12M28 22l-4 4M28 22l4 4"/><path d="M24 20c-6 0-10 9-10 17 0 3 3 3 6 1l4-3z"/><path d="M32 20c6 0 10 9 10 17 0 3-3 3-6 1l-4-3z"/></svg>Lungenfunktionsuntersuchung</li>
    <li><svg viewBox="0 0 56 56" fill="none" stroke="var(--pink)" stroke-width="1.6"><circle cx="28" cy="28" r="26.5"/><circle cx="26" cy="15" r="3"/><path d="M16 22h20M22 22v20M30 22v8"/><circle cx="34" cy="34" r="4"/><path d="M37 37l4 4"/></svg>Hautkrebsscreening</li>
    <li><svg viewBox="0 0 56 56" fill="none" stroke="var(--pink)" stroke-width="1.6"><circle cx="28" cy="28" r="26.5"/><path d="M16 40l4-4M19 33l7 7M23 36l14-14-4-4-14 14"/><path d="M35 16l5 5M37 18l3-3"/><path d="M40 25q2 3 0 4q-2-1 0-4z"/></svg>Impfberatung/Reisemedizin</li>
  </ul>
</div>
</body>
</html>
```